Business Card Design Project

Business Card
We are rebranding with a new logo
Industry/Entity Type
Business
Contact Information for Business Card
Dennis Marlow +61 427581962 dennis@qovo.com.au P.O. Box 872 Kelvindale QLD 4309
Requirements
Must have
- Logo

```html
<!DOCTYPE html>
<html lang="en">
<head>
<meta charset="utf-8">
<title>Qovo International – Business Card</title>
<link href="https://fonts.googleapis.com/css2?family=Ubuntu:wght@400;700&display=swap" rel="stylesheet">
<style>
  :root {
    --backdrop: #2b2b2d;
    --card-base: #3a3b3e;
    --brand-blue: #1f9fd0;
    --brand-blue-deep: #1784b3;
    --brand-orange: #f0901f;
    --brand-orange-deep: #e2701c;
    --text-light: #ffffff;
  }
  html, body {
    margin: 0;
    width: 1200px;
    height: 1200px;
    overflow: hidden;
    background: var(--backdrop);
  }
  .canvas {
    position: relative;
    width: 1200px;
    height: 1200px;
  }
  .business-card {
    position: absolute;
    left: 150px;
    top: 343px;
    width: 900px;
    height: 514px;
    border-radius: 22px;
    overflow: hidden;
    background: var(--card-base);
    box-shadow: 0 20px 50px rgba(0,0,0,0.45);
    font-family: "Ubuntu", sans-serif;
  }
  .card-art {
    position: absolute;
    inset: 0;
  }
  .contact-block {
    position: absolute;
    left: 64px;
    top: 48px;
    color: var(--text-light);
  }
  .contact-name {
    margin: 0 0 22px;
    font-size: 38px;
    font-weight: 700;
    letter-spacing: 1.5px;
    text-transform: uppercase;
  }
  .contact-line {
    margin: 0 0 8px;
    font-size: 25px;
    font-weight: 400;
    letter-spacing: 0.3px;
  }
  .brand-lockup {
    position: absolute;
    right: 70px;
    bottom: 70px;
    display: flex;
    align-items: center;
    gap: 18px;
    color: var(--brand-blue);
    font-weight: 700;
  }
  .brand-dot {
    width: 34px;
    height: 34px;
    border-radius: 50%;
    background: var(--brand-blue);
  }
  .brand-name {
    font-size: 40px;
    letter-spacing: 3px;
    text-transform: uppercase;
  }
</style>
</head>
<body>
<main class="canvas">
  <section class="business-card">
    <svg class="card-art" viewBox="0 0 900 514" preserveAspectRatio="none" aria-hidden="true">
      <path class="blue-field" d="M0 0 H900 V20 Q520 90 270 514 H0 Z" fill="var(--brand-blue)"/>
      <path class="blue-shade" d="M0 220 Q300 180 900 20 Q520 90 270 514 H0 Z" fill="var(--brand-blue-deep)" opacity="0.35"/>
      <path class="orange-shape" d="M0 300 H170 Q235 300 245 350 Q255 420 215 514 H0 Z" fill="var(--brand-orange)"/>
      <path class="orange-shade" d="M170 300 Q235 300 245 350 Q255 420 215 514 H185 Q225 420 215 360 Q205 318 150 300 Z" fill="var(--brand-orange-deep)"/>
    </svg>
    <div class="contact-block">
      <h1 class="contact-name">Dennis Marlow</h1>
      <p class="contact-line">+61 427581962</p>
      <p class="contact-line">dennis@qovo.com.au</p>
      <p class="contact-line">P.O. Box 872 Kelvindale QLD 4309</p>
    </div>
    <div class="brand-lockup">
      <span class="brand-dot"></span>
      <span class="brand-name">Qovo International</span>
    </div>
  </section>
</main>
</body>
</html>
```